Financial Advisor Resource Firm needs business card design

Need business card design for company in Omaha NE called Tallowbrook Partners. We provide resources to financial advisors....workshop programs, retirement analysis, and insurance planning. I would like to see designs that use grays, greens, black, and white colors. The final design should communicate 'collaboration' and be simple yet attractive to financial planning clients. I will attached our logo and another picture of a puzzle piece coming together. I would like the incorporate the puzzle picture somehow, maybe on the back somehow, with color or just the gray scale....OR, the picture be the front of the card with 'Tallowbrook' definition on it (see upload) and then company logo, employee name, title, address on the back (see ppt uploaded). The following disclosure needs to be included somewhere- Advisory services offered through Marlowe Ridge Advisors, LLC.
Updates

I uploaded a svg and ai file of the logo

Target Market(s)

Financial planning clients and financial advisors....so pretty diverse age range of about 40-70.

Industry/Entity Type

Financial Planning

Contact Information for Business Card

Dennis K. Holloway, MBA
Founder/President
5727 E. Larkspur Avenue
Suite 418
Omaha, NE 68297
Phone- (402) 555-0147
Cell- (402) 555-0183
Fax- (402) 555-0129
email- dennis@tallowbrookgroup.example
web address- www.tallowbrookgroup.example

Colors
1b1b1b
474747
d3d3d3
ffffff
9bcb3c
abd036

Requirements
Must have
• Must include logo provided, must be 2 sided, and must have disclosure...all of these items listed in project description

```html
<!DOCTYPE html>
<html lang="en">
<head>
<meta charset="utf-8">
<title>Tallowbrook Partners – Business Card</title>
<link href="https://fonts.googleapis.com/css2?family=Roboto:wght@400;500;700&display=swap" rel="stylesheet">
<style>
  :root {
    --stage: #3d3d3d;
    --ink: #1b1b1b;
    --charcoal: #2e2e2e;
    --gray: #474747;
    --light-gray: #d3d3d3;
    --white: #ffffff;
    --green: #9bcb3c;
    --green-band: #8cc03a;
  }
  * { margin: 0; padding: 0; box-sizing: border-box; }
  html, body {
    width: 1200px; height: 1000px; overflow: hidden;
    background: var(--stage);
    font-family: "Roboto", Arial, sans-serif;
  }
  .card {
    position: absolute; left: 250px;
    width: 700px; height: 400px;
    border-radius: 20px; overflow: hidden;
    box-shadow: 0 10px 30px rgba(0,0,0,.35);
  }

  /* Front */
  .card-front { top: 70px; background: var(--white); }
  .front-photo {
    position: absolute; inset: 0;
    background: radial-gradient(ellipse at 40% 60%, #c9c9c9 0%, #e4e4e4 45%, #f4f4f4 100%);
  }
  .front-wordmark {
    position: absolute; left: 0; right: 0; top: 165px;
    text-align: center;
    font-size: 46px; font-weight: 500; letter-spacing: 2px;
    text-transform: uppercase; color: var(--ink);
  }
  .front-band {
    position: absolute; left: 0; right: 0; top: 312px; height: 40px;
    background: var(--green-band);
    display: flex; align-items: center; justify-content: center;
  }
  .front-tagline { font-size: 18px; font-weight: 700; color: var(--ink); }

  /* Back */
  .card-back { top: 530px; background: linear-gradient(135deg, #262626 0%, var(--charcoal) 60%, #333 100%); }
  .holder { position: absolute; left: 52px; top: 44px; }
  .holder-name {
    font-size: 26px; font-weight: 700; color: var(--green);
    text-transform: uppercase; letter-spacing: .5px;
  }
  .holder-name .credential { font-size: 17px; }
  .holder-title { font-size: 17px; color: var(--white); margin-top: 4px; }
  .divider {
    position: absolute; left: 52px; top: 140px;
    width: 62px; height: 2px; background: var(--green);
  }
  .contact { position: absolute; left: 52px; top: 196px; color: var(--white); font-size: 15px; line-height: 21px; }
  .contact-address { margin-left: 24px; margin-bottom: 2px; }
  .contact-row { display: flex; align-items: center; gap: 8px; }
  .contact-row svg { width: 16px; height: 16px; flex: none; }
  .disclosure {
    position: absolute; left: 52px; top: 364px;
    font-size: 11px; color: var(--light-gray); white-space: nowrap;
  }
  .back-wordmark {
    position: absolute; right: 40px; top: 272px;
    font-size: 40px; font-weight: 500; letter-spacing: 2px;
    text-transform: uppercase; color: var(--white);
  }
  .back-band {
    position: absolute; left: 390px; right: 0; top: 330px; height: 26px;
    background: var(--green-band);
  }
</style>
</head>
<body>

<section class="card card-front">
  <div class="front-photo" role="img" aria-label="Grayscale photograph of hands fitting puzzle pieces together"></div>
  <div class="front-wordmark">Tallowbrook Partners</div>
  <div class="front-band">
    <p class="front-tagline">to come together and unite in common interest and focus</p>
  </div>
</section>

<section class="card card-back">
  <div class="holder">
    <h1 class="holder-name">Dennis K. Holloway, <span class="credential">MBA</span></h1>
    <p class="holder-title">Founder/President</p>
  </div>
  <div class="divider"></div>

  <div class="contact">
    <p class="contact-address">5727 E. Larkspur Avenue<br>Suite 418 Omaha, NE 68297</p>
    <p class="contact-row">
      <svg viewBox="0 0 16 16" fill="none" stroke="#9bcb3c" stroke-width="1.5"><path d="M4 2l2 3-1.5 1.5a8 8 0 0 0 5 5L11 10l3 2-1.5 2.5C7 14 2 9 1.5 3.5z"/></svg>
      (402) 555-0147
    </p>
    <p class="contact-row">
      <svg viewBox="0 0 16 16" fill="none" stroke="#9bcb3c" stroke-width="1.5"><rect x="4.5" y="1.5" width="7" height="13" rx="1.2"/><line x1="7" y1="12.5" x2="9" y2="12.5"/></svg>
      (402) 555-0183
    </p>
    <p class="contact-row">
      <svg viewBox="0 0 16 16" fill="none" stroke="#9bcb3c" stroke-width="1.5"><rect x="4" y="1.5" width="8" height="5"/><rect x="1.5" y="6.5" width="13" height="6" rx="1"/><rect x="4" y="10.5" width="8" height="4"/></svg>
      (402) 555-0129
    </p>
    <p class="contact-row">
      <svg viewBox="0 0 16 16" fill="none" stroke="#9bcb3c" stroke-width="1.5"><rect x="1.5" y="3.5" width="13" height="9" rx="1"/><path d="M1.5 4l6.5 5 6.5-5"/></svg>
      dennis@tallowbrookgroup.example
    </p>
    <p class="contact-row">
      <svg viewBox="0 0 16 16" fill="none" stroke="#9bcb3c" stroke-width="1.3"><circle cx="8" cy="8" r="6.5"/><ellipse cx="8" cy="8" rx="3" ry="6.5"/><line x1="1.5" y1="8" x2="14.5" y2="8"/></svg>
      www.tallowbrookgroup.example
    </p>
  </div>

  <p class="disclosure">Advisory services offered through Marlowe Ridge Advisors, LLC</p>

  <div class="back-wordmark">Tallowbrook</div>
  <div class="back-band"></div>
</section>

</body>
</html>
```